BOLD Gym Needs a New WALL WRAP!

We have a small wall that we need to spice up and we'd like to wrap it with a bold design that stands out and breaks up the current bland grey color.
The wall itself is 128.25" long x 50.5" tall
I am open to design options, but the design must include our ZorvaLyft logo (attached)
I have also included photos of the gym to give you an idea of the vibe, colors, etc.
DO NOT BE AFRAID OF COLOR😊​ Although our colors are Yellow, Grey's, Blacks, etc., in the gym, please do not be afraid to play with color while still making it look like it belongs in our building. The posters that hang around that wall have pinks, purples, etc. in it. I've included a poster for you to see the colors that are nearby.
The photo from the ground looking up towards the second story highlights the wall that needs to be wrapped.
The ultimate goal here is to break up the grey wall with a killer design.

```html
<!DOCTYPE html>
<html lang="en">
<head>
<meta charset="utf-8">
<title>ZorvaLyft Wall Wrap</title>
<link rel="stylesheet" href="https://fonts.googleapis.com/css2?family=Black+Ops+One&family=Montserrat:wght@800;900&display=swap">
<style>
  :root {
    --ink: #000000;
    --brand-yellow: #f9d000;
    --brand-white: #ffffff;
  }
  html, body {
    margin: 0;
    padding: 0;
    overflow: hidden;
    background: var(--ink);
  }
  .wall-wrap {
    display: block;
    width: 1200px;
    height: 472px;
    background: var(--ink);
  }
  .paint-band { fill: var(--brand-yellow); }
  .paint-streak { fill: var(--brand-yellow); }
  .brand-name {
    font-family: "Montserrat", sans-serif;
    font-weight: 900;
    font-size: 184px;
    fill: var(--brand-white);
  }
  .brand-tagline {
    font-family: "Montserrat", sans-serif;
    font-weight: 800;
    font-size: 19px;
    fill: var(--brand-yellow);
  }
  .headline {
    font-family: "Black Ops One", sans-serif;
    font-size: 116px;
    fill: var(--ink);
  }
</style>
</head>
<body>
<svg class="wall-wrap" viewBox="0 0 1200 472" width="1200" height="472" xmlns="http://www.w3.org/2000/svg">
  <!-- yellow paint band -->
  <polygon class="paint-band" points="0,236 60,232 180,234 300,230 420,231 520,228 640,229 760,227 880,229 1000,228 1100,230 1200,229 1200,448 1130,450 1020,447 900,451 780,448 660,452 540,449 420,452 300,449 180,451 60,448 0,450"/>
  <rect class="paint-streak" x="0" y="228" width="260" height="3"/>
  <rect class="paint-streak" x="700" y="224" width="320" height="3"/>
  <rect class="paint-streak" x="1050" y="225" width="150" height="2"/>
  <rect class="paint-streak" x="120" y="453" width="380" height="3"/>
  <rect class="paint-streak" x="820" y="455" width="260" height="2"/>

  <!-- brand name -->
  <text class="brand-name" x="328" y="177" textLength="590" lengthAdjust="spacingAndGlyphs">ZorvaLyft</text>
  <text class="brand-tagline" x="427" y="216" textLength="389" lengthAdjust="spacing">PERSONAL GROUP TRAINING</text>

  <!-- headline -->
  <text class="headline" x="126" y="337" textLength="961" lengthAdjust="spacingAndGlyphs">CHALLENGE YOURSELF,</text>
  <text class="headline" x="196" y="441" textLength="821" lengthAdjust="spacingAndGlyphs">CHANGE YOURSELF.</text>
</svg>
</body>
</html>
```